Web page design/layout for dog breeder

We are looking for a new layout/design for our current web page. Current web pages can be found at http://ruddyhound.sitefold.com.

We recently uploaded the PTR Kennel of Renown banner that we would like to have displayed on the home page.

```html
<!DOCTYPE html>
<html lang="en">
<head>
<meta charset="utf-8">
<title>Ruddyhound – Home</title>
<link href="https://fonts.googleapis.com/css2?family=Open+Sans:wght@400;600&display=swap" rel="stylesheet">
<style>
  :root {
    --canvas: #ffffff;
    --page: #ffffff;
    --pattern: #f6e9e7;
    --pattern-edge: #ead3cf;
    --ink: #222222;
    --accent: #7a1414;
    --band: #000000;
    --band-panel: #121212;
    --brand: #d9d9d9;
    --ring: #3a3a3a;
  }
  * { box-sizing: border-box; margin: 0; padding: 0; }
  html, body {
    width: 1200px; height: 847px; overflow: hidden;
    background: var(--canvas);
    font-family: "Open Sans", Arial, sans-serif;
    color: var(--ink);
  }
  .site {
    position: absolute; left: 91px; top: 39px;
    width: 1018px; height: 808px;
    background: var(--page);
  }
  .side-pattern {
    position: absolute; top: 0; bottom: 0; width: 112px;
    background: linear-gradient(180deg, var(--pattern), var(--pattern-edge) 50%, var(--pattern));
  }
  .side-pattern--left { left: 0; }
  .side-pattern--right { right: 0; }
  .main-nav {
    position: absolute; top: 68px; left: 0; width: 100%;
    font-size: 22px; line-height: 32px;
  }
  .main-nav a {
    position: absolute; color: var(--ink); text-decoration: none; white-space: nowrap;
  }
  .main-nav a.is-current { color: var(--accent); }
  .brand-band {
    position: absolute; left: 0; top: 118px; width: 100%; height: 99px;
    background: var(--band);
  }
  .brand-panel {
    position: absolute; left: 243px; top: 0; width: 548px; height: 99px;
    background: var(--band-panel);
    display: flex; align-items: center; justify-content: center; gap: 12px;
  }
  .brand-mark {
    width: 14px; height: 14px; border-radius: 50%;
    background: var(--brand);
  }
  .brand-name {
    color: var(--brand); font-size: 20px; font-weight: 600; letter-spacing: 2px;
  }
  .section-hub {
    position: absolute; left: 0; top: 0;
  }
  .hub-label {
    font-family: "Open Sans", Arial, sans-serif;
    font-size: 22px; fill: var(--ink);
  }
  .hub-ring { fill: none; stroke: var(--ring); stroke-width: 3; }
</style>
</head>
<body>
<div class="site">
  <div class="side-pattern side-pattern--left" role="img" aria-label="Decorative red swirl pattern border"></div>
  <div class="side-pattern side-pattern--right" role="img" aria-label="Decorative red swirl pattern border"></div>

  <nav class="main-nav">
    <a class="is-current" href="#" style="left:123px">Home</a>
    <a href="#" style="left:212px">Our Story</a>
    <a href="#" style="left:334px">Our Vizslas</a>
    <a href="#" style="left:473px">New Arrivals</a>
    <a href="#" style="left:627px">Photo Gallery</a>
    <a href="#" style="left:789px">Contact Us</a>
  </nav>

  <header class="brand-band">
    <div class="brand-panel">
      <span class="brand-mark"></span>
      <span class="brand-name">RUDDYHOUND</span>
    </div>
  </header>

  <svg class="section-hub" width="1018" height="808" viewBox="91 39 1018 808">
    <defs>
      <radialGradient id="g-hero" cx="50%" cy="50%" r="50%">
        <stop offset="0" stop-color="#b0652e"/><stop offset="0.45" stop-color="#8a6a35"/><stop offset="1" stop-color="#4f8a2e"/>
      </radialGradient>
      <radialGradient id="g-arrivals" cx="50%" cy="50%" r="50%">
        <stop offset="0" stop-color="#c2612c"/><stop offset="1" stop-color="#2b2624"/>
      </radialGradient>
      <radialGradient id="g-story" cx="50%" cy="50%" r="50%">
        <stop offset="0" stop-color="#6e4a33"/><stop offset="1" stop-color="#9aa393"/>
      </radialGradient>
      <radialGradient id="g-gallery" cx="50%" cy="50%" r="50%">
        <stop offset="0" stop-color="#b3622f"/><stop offset="1" stop-color="#6b4a30"/>
      </radialGradient>
      <radialGradient id="g-vizslas" cx="50%" cy="50%" r="50%">
        <stop offset="0" stop-color="#a9572a"/><stop offset="1" stop-color="#6a4a2e"/>
      </radialGradient>
      <radialGradient id="g-contact" cx="50%" cy="50%" r="50%">
        <stop offset="0" stop-color="#b8522a"/><stop offset="0.7" stop-color="#c0303a"/><stop offset="1" stop-color="#f4f0ee"/>
      </radialGradient>
      <path id="arc-arrivals" d="M542,339 A64,64 0 0,1 668,339"/>
      <path id="arc-story" d="M334,500 A65,65 0 0,1 462,500"/>
      <path id="arc-gallery" d="M745,477 A66,66 0 0,1 873,500"/>
      <path id="arc-vizslas" d="M417,694 A67,67 0 0,1 549,694"/>
      <path id="arc-contact" d="M665,695 A66,66 0 0,1 795,695"/>
    </defs>

    <circle cx="605" cy="535" r="97" fill="url(#g-hero)" role="img" aria-label="Vizsla puppy sitting on green grass"/>
    <circle class="hub-ring" cx="605" cy="535" r="97"/>

    <circle cx="605" cy="350" r="56" fill="url(#g-arrivals)" role="img" aria-label="Litter of newborn vizsla puppies"/>
    <circle class="hub-ring" cx="605" cy="350" r="56"/>
    <text class="hub-label"><textPath href="#arc-arrivals" startOffset="50%" text-anchor="middle">New Arrivals</textPath></text>

    <circle cx="398" cy="511" r="57" fill="url(#g-story)" role="img" aria-label="Breeder outdoors with a vizsla"/>
    <circle class="hub-ring" cx="398" cy="511" r="57"/>
    <text class="hub-label"><textPath href="#arc-story" startOffset="50%" text-anchor="middle">Our Story</textPath></text>

    <circle cx="807" cy="500" r="58" fill="url(#g-gallery)" role="img" aria-label="Portrait of a vizsla"/>
    <circle class="hub-ring" cx="807" cy="500" r="58"/>
    <text class="hub-label"><textPath href="#arc-gallery" startOffset="50%" text-anchor="middle">Photo Gallery</textPath></text>

    <circle cx="483" cy="706" r="58" fill="url(#g-vizslas)" role="img" aria-label="Adult vizsla portrait"/>
    <circle class="hub-ring" cx="483" cy="706" r="58"/>
    <text class="hub-label"><textPath href="#arc-vizslas" startOffset="50%" text-anchor="middle">Our Vizslas</textPath></text>

    <circle cx="730" cy="706" r="58" fill="url(#g-contact)" role="img" aria-label="Vizsla holding a red toy"/>
    <circle class="hub-ring" cx="730" cy="706" r="58"/>
    <text class="hub-label"><textPath href="#arc-contact" startOffset="50%" text-anchor="middle">Contact</textPath></text>
  </svg>
</div>
</body>
</html>
```